Modern business card design for professional copywriter

I'd like a business card design that I can use to have my cards printed out by tavrel.com as a squared corners business card (see artwork and design guidelines here: https://help.tavrel.com/hc/en-gb/sections/300481762-TAVREL-Product-Templates)

The design should be clean and modern and reflect the colours, tone and branding on my website: https://gretafolvane.com.au

Target Market(s)

Professionals, B2B small business owners

Industry/Entity Type

Business

Contact Information for Business Card

Greta Folvane
m: 0427 954 368
e: greta@gretafolvane.com.au
w: gretafolvane.com.au

Font styles to use
Sans Serif

Requirements
Must have
• Tagline: "Sharp words for busy, ambitious business owners"
• Brand colours: fd8000, 009984, 666666 and black
Nice to have

```html
<!DOCTYPE html>
<html lang="en">
<head>
<meta charset="utf-8">
<title>Greta Folvane – Business Card</title>
<link href="https://fonts.googleapis.com/css2?family=Montserrat:wght@300;400;700&display=swap" rel="stylesheet">
<style>
  :root {
    --orange: #fd8000;
    --teal: #009984;
    --grey: #666666;
    --backdrop: #a7a8ab;
    --paper: #ffffff;
  }
  * { margin: 0; padding: 0; box-sizing: border-box; }
  html, body { width: 1200px; height: 927px; overflow: hidden; }
  body {
    background: var(--backdrop);
    font-family: "Montserrat", sans-serif;
    position: relative;
  }
  .card {
    position: absolute;
    left: 270px;
    width: 648px;
    height: 370px;
    background: var(--paper);
  }
  .card--front { top: 71px; }
  .card--back { top: 486px; }

  .brand {
    position: absolute;
    display: flex;
    align-items: center;
    gap: 8px;
    font-family: "Montserrat", sans-serif;
    font-weight: 400;
    font-size: 28px;
    letter-spacing: -0.5px;
    color: var(--teal);
    white-space: nowrap;
  }
  .brand__dot {
    width: 18px; height: 18px;
    border-radius: 50%;
    background: var(--orange);
  }
  .card--front .brand { right: 38px; top: 94px; }
  .card--back .brand { left: 50%; top: 158px; transform: translateX(-50%); }

  .holder-name {
    position: absolute;
    left: 50px; top: 220px;
    font-weight: 700;
    font-size: 29px;
    color: var(--orange);
  }
  .rule {
    position: absolute;
    left: 50px; top: 266px;
    width: 551px; height: 2px;
    background: var(--teal);
  }
  .contacts {
    position: absolute;
    left: 50px; top: 280px;
    list-style: none;
  }
  .contacts li {
    display: flex;
    align-items: center;
    height: 22px;
    font-weight: 300;
    font-size: 19px;
    color: var(--orange);
  }
  .contacts svg { width: 16px; height: 16px; margin-right: 16px; flex: none; }
  .contacts .accent { color: var(--teal); }

  .tagline {
    position: absolute;
    left: 0; right: 0; top: 221px;
    text-align: center;
    font-weight: 400;
    font-size: 18px;
    color: var(--orange);
  }
</style>
</head>
<body>
  <section class="card card--front">
    <div class="brand"><span class="brand__dot"></span>Greta Folvane</div>
    <h1 class="holder-name">Greta Folvane</h1>
    <div class="rule"></div>
    <ul class="contacts">
      <li>
        <svg viewBox="0 0 16 16" aria-hidden="true"><circle cx="8" cy="8" r="8" fill="var(--teal)"/><rect x="5.2" y="3.2" width="5.6" height="9.6" rx="1" fill="none" stroke="#fff" stroke-width="1.2"/><circle cx="8" cy="11.2" r="0.7" fill="#fff"/></svg>
        0427 954 368
      </li>
      <li>
        <svg viewBox="0 0 16 16" aria-hidden="true"><circle cx="8" cy="8" r="8" fill="var(--teal)"/><rect x="4" y="5" width="8" height="6" rx="0.8" fill="none" stroke="#fff" stroke-width="1.1"/><path d="M4.3 5.5 8 8.5l3.7-3" fill="none" stroke="#fff" stroke-width="1.1"/></svg>
        <span><span class="accent">greta@gretafolvane</span>.com.au</span>
      </li>
      <li>
        <svg viewBox="0 0 16 16" aria-hidden="true"><circle cx="8" cy="8" r="8" fill="var(--teal)"/><g fill="none" stroke="#fff" stroke-width="0.9"><circle cx="8" cy="8" r="4.5"/><ellipse cx="8" cy="8" rx="2" ry="4.5"/><path d="M3.5 8h9M4.2 5.8h7.6M4.2 10.2h7.6"/></g></svg>
        gretafolvane.com.au
      </li>
    </ul>
  </section>

  <section class="card card--back">
    <div class="brand"><span class="brand__dot"></span>Greta Folvane</div>
    <p class="tagline">"Sharp words for busy, ambitious business owners"</p>
  </section>
</body>
</html>
```